Welland Dental, P.C. New stationary and business card for modern Dental Office

We need a new stationary/envelope/business card design using our newly designed logo. We are looking for an upscale look. Our new logo is used on our signage, using black as the background and white for the lettering. We would like the stationary to have black, white, possible greys or silver. We are looking for a letterhead, envelope, and business card design for three different employees, as well as a 4th card, same design, but just general with no employee name.
Updates

Project Deadline Extended
Reason: We began this project in the middle of our move into our new office. Things got pretty hectic and we just didn't have the time to go through designs. We now settled in and finally eliminated the designs that didn't work for us. We would like to extend the project another 5 days, and then finalize our decision. Most of the submissions showed business cards alone, with no stationary designs. Our original request was for stationary and business cards. Please keep this in mind.

Target Market(s)

Dental patients expecting high quality, cosmetic dentistry

Industry/Entity Type

Business

Contact Information for Business Card

Will need a design using our logo. All cards will be the same, other than that one card will have Office Managers name, One for the Doctor, Hygienist,
1. Office Manager - Marisol Penrose
2. Hygienist - Courtney Whitlock
3. Owen T. Welland, D.D.S.
4. One general one with no staff names

Font styles to use
Other font styles liked:
• see upload

Colors
000000
1b1b1b
757575
c9c9c9
e8e8e8
ffffff

Requirements
Must have
• -Logo
• -Phone number (718)555-0143
• -Address: 4392 63rd Ave
• Lower Level
• Brooklyn, NY 11398

```html
<!DOCTYPE html>
<html lang="en">
<head>
<meta charset="utf-8">
<title>Welland Dental, P.C. – Business Cards</title>
<link rel="stylesheet" href="https://fonts.googleapis.com/css2?family=Source+Sans+3:wght@400;600;700&display=swap">
<style>
  :root {
    --bg: #ece9e6;
    --card-dark: #2f2a29;
    --card-light: #dcd7d2;
    --text-light: #ffffff;
    --text-dark: #2a2f33;
  }
  html, body {
    margin: 0;
    padding: 0;
    width: 1200px;
    height: 900px;
    overflow: hidden;
    background: var(--bg);
    font-family: "Source Sans 3", "Myriad Pro", sans-serif;
  }
  .canvas {
    position: relative;
    width: 1200px;
    height: 900px;
  }
  .card {
    position: absolute;
    border-radius: 14px;
    overflow: hidden;
    box-shadow: 0 6px 18px rgba(0,0,0,0.18);
  }
  .card--front {
    left: 78px; top: 35px; width: 588px; height: 363px;
    background: var(--card-dark);
    color: var(--text-light);
  }
  .card--back {
    left: 388px; top: 506px; width: 567px; height: 350px;
    background: var(--card-light);
    color: var(--text-dark);
  }
  .card__band { position: absolute; left: 0; top: 0; }
  .brand {
    position: absolute;
    display: flex;
    align-items: center;
    gap: 10px;
    font-weight: 600;
    white-space: nowrap;
  }
  .card--front .brand { left: 0; width: 588px; top: 108px; justify-content: center; font-size: 28px; color: var(--text-light); }
  .card--back .brand { left: 0; width: 567px; top: 616px; top: 110px; justify-content: center; font-size: 27px; color: var(--text-dark); }
  .brand__dot {
    width: 14px; height: 14px; border-radius: 50%;
    border: 2px solid currentColor;
  }
  .contact {
    position: absolute;
    left: 0; width: 588px;
    text-align: center;
  }
  .contact__name { top: 211px; font-size: 20px; font-weight: 700; letter-spacing: 0.3px; }
  .contact__role { top: 238px; font-size: 16px; }
  .contact__phone { top: 281px; font-size: 16px; display: flex; justify-content: center; align-items: center; gap: 4px; }
  .contact__address { top: 322px; font-size: 16px; }
</style>
</head>
<body>
<main class="canvas">
  <section class="card card--front" aria-label="Business card front">
    <svg class="card__band" width="588" height="363" viewBox="0 0 588 363" aria-hidden="true">
      <rect x="0" y="45" width="588" height="100" fill="var(--card-light)"/>
      <rect x="112" y="45" width="343" height="100" rx="50" fill="var(--card-dark)"/>
    </svg>
    <div class="brand"><span>Welland Dental, P.C.</span><span class="brand__dot"></span></div>
    <div class="contact contact__name">DANIEL MARSH</div>
    <div class="contact contact__role">Managing Director</div>
    <div class="contact contact__phone">
      <svg width="12" height="12" viewBox="0 0 24 24" aria-hidden="true"><path fill="#fff" d="M6.6 10.8a15.2 15.2 0 0 0 6.6 6.6l2.2-2.2a1 1 0 0 1 1-.25 11.4 11.4 0 0 0 3.6.57 1 1 0 0 1 1 1V20a1 1 0 0 1-1 1A17 17 0 0 1 3 4a1 1 0 0 1 1-1h3.5a1 1 0 0 1 1 1c0 1.25.2 2.45.57 3.57a1 1 0 0 1-.25 1z"/></svg>
      <span>(718)555-0143</span>
    </div>
    <div class="contact contact__address">4392 63rd Ave Lower Level Brooklyn, NY 11398</div>
  </section>

  <section class="card card--back" aria-label="Business card back">
    <svg class="card__band" width="567" height="350" viewBox="0 0 567 350" aria-hidden="true">
      <rect x="0" y="81" width="567" height="96" fill="var(--card-dark)"/>
      <rect x="115" y="81" width="323" height="96" rx="48" fill="var(--card-light)"/>
    </svg>
    <div class="brand"><span>Welland Dental, P.C.</span><span class="brand__dot"></span></div>
  </section>
</main>
</body>
</html>
```